uPalShield Advert, internet security for children.

we need a newspaper/magazine advert approx. size 150mm wide by 110mm high

uPalShield is a service used to protect children online when using all types of devices, on Wi-Fi and mobile network connections.

the website is www.upalshield.co.uk

The ad should communicate ease of use, and should be aimed at parents with children between the ages of 3-18

attached logo designs.

Target Market(s)

Parents with children aged 3-18

Industry/Entity Type

Internet

Font styles to use
Serif
Sans Serif

Requirements
Must have
• company logo, website address, platforms service works on, android, iOS etc. free 30 day trial.
Nice to have
• email address of info@upalshield.co.uk
Should not have
• phone numbers, pricing.

```html
<!DOCTYPE html>
<html lang="en">
<head>
<meta charset="utf-8">
<title>uPalShield – Protect your children from the web</title>
<link rel="stylesheet" href="https://fonts.googleapis.com/css2?family=Archivo+Black&family=Open+Sans:wght@300;400;600;700&display=swap">
<style>
  :root {
    --navy: #163f5a;
    --brand: #1f4f6b;
    --sky: #2a9fd8;
    --sky-light: #5cc1ea;
    --paper: #ffffff;
    --photo-warm: #c9b4a0;
    --photo-cool: #d8d6d2;
  }
  * { margin: 0; padding: 0; box-sizing: border-box; }
  html, body { width: 1200px; height: 880px; overflow: hidden; background: var(--paper); }
  .advert {
    position: relative;
    width: 1200px;
    height: 880px;
    background: var(--paper);
    font-family: "Open Sans", Arial, sans-serif;
    color: var(--navy);
    overflow: hidden;
  }
  .hero { position: absolute; left: 0; top: 0; width: 1200px; height: 880px; }

  .brand {
    position: absolute; right: 32px; top: 38px;
    display: flex; align-items: center; gap: 18px;
  }
  .brand-dot { width: 64px; height: 64px; border-radius: 50%; background: var(--sky); }
  .brand-name {
    font-family: "Open Sans", Arial, sans-serif;
    font-weight: 700; font-size: 58px; letter-spacing: 1px;
    color: var(--brand);
  }

  .headline {
    position: absolute; right: 30px; top: 178px;
    font-family: "Archivo Black", Arial, sans-serif;
    font-size: 47px; line-height: 1.17;
    text-align: right; color: var(--navy);
  }

  .feature {
    position: absolute; right: 30px;
    display: flex; align-items: center; gap: 14px;
    font-weight: 300; font-size: 41px; line-height: 1.08;
    color: var(--navy); text-align: right;
  }
  .feature--easy { top: 340px; }
  .feature--safe { top: 448px; }
  .feature svg { flex: none; }

  .trial {
    position: absolute; right: 30px; top: 572px;
    text-align: right; line-height: 1.02;
  }
  .trial-offer { font-weight: 700; font-size: 45px; color: var(--sky); }
  .trial-term { font-weight: 400; font-size: 37px; color: var(--navy); }

  .contact {
    position: absolute; right: 30px; top: 702px;
    text-align: right;
  }
  .contact-lead { font-size: 24px; font-weight: 400; color: var(--navy); }
  .contact-email { font-size: 26px; font-weight: 400; color: var(--sky); letter-spacing: 0.3px; }

  .platforms {
    position: absolute; right: 82px; top: 818px;
    display: flex; gap: 22px; list-style: none;
  }
  .platform { width: 48px; height: 48px; border-radius: 8px; background: var(--sky); }
</style>
</head>
<body>
<main class="advert">
  <svg class="hero" viewBox="0 0 1200 880" aria-hidden="false">
    <defs>
      <linearGradient id="photoTone" x1="0" y1="0" x2="1" y2="1">
        <stop offset="0" stop-color="var(--photo-cool)"/>
        <stop offset="0.55" stop-color="var(--photo-warm)"/>
        <stop offset="1" stop-color="#a98a70"/>
      </linearGradient>
      <linearGradient id="frameTone" x1="0" y1="0" x2="1" y2="1">
        <stop offset="0" stop-color="var(--sky-light)"/>
        <stop offset="0.6" stop-color="var(--sky)"/>
        <stop offset="1" stop-color="#1d5a7e"/>
      </linearGradient>
    </defs>
    <path role="img" aria-label="Photo of two young children looking at a laptop screen together"
      d="M0 100 C 90 60 190 45 260 62 C 320 80 365 150 370 250 C 400 215 460 215 500 240 C 560 260 600 285 610 330 C 660 370 690 420 680 470 C 710 520 720 560 715 600 C 740 640 750 680 745 720 C 755 780 760 830 762 880 L 0 880 Z"
      fill="url(#photoTone)" stroke="url(#frameTone)" stroke-width="14"/>
  </svg>

  <div class="brand">
    <span class="brand-dot"></span>
    <span class="brand-name">uPalShield</span>
  </div>

  <h1 class="headline">Protect your children<br>from the web.</h1>

  <div class="feature feature--easy">
    <svg width="84" height="84" viewBox="0 0 84 84" aria-hidden="true">
      <circle cx="42" cy="42" r="38" fill="none" stroke="var(--sky)" stroke-width="5"/>
      <path d="M24 42 L37 57 L61 24" fill="none" stroke="var(--sky)" stroke-width="8" stroke-linecap="round" stroke-linejoin="round"/>
    </svg>
    <span>Easy to use</span>
  </div>

  <div class="feature feature--safe">
    <svg width="76" height="84" viewBox="0 0 76 84" aria-hidden="true">
      <path d="M5 12 C 20 10 30 7 38 3 C 46 7 56 10 71 12 C 71 46 60 68 38 81 C 16 68 5 46 5 12 Z" fill="none" stroke="var(--sky)" stroke-width="5" stroke-linejoin="round"/>
    </svg>
    <span>Safe for<br>children</span>
  </div>

  <div class="trial">
    <div class="trial-offer">FREE 30</div>
    <div class="trial-term">days trial</div>
  </div>

  <div class="contact">
    <p class="contact-lead">For more info visit us</p>
    <p class="contact-email">info@upalshield.co.uk</p>
  </div>

  <ul class="platforms" aria-label="Supported platforms">
    <li class="platform"></li>
    <li class="platform"></li>
    <li class="platform"></li>
    <li class="platform"></li>
  </ul>
</main>
</body>
</html>
```